Business Cards

Business cards (double-sided) to be handed out to clients and potential clients, with contact details, logo .

Target Market(s)

Small to medium size businesses

Industry/Entity Type

Accountants

Contact Information for Business Card

Brightwater Ledger & Counsel Ltd

Colors

Designer to choose only greyscale colors for use in the design.

Requirements
Must have
• Name, Title, Address, Phone number, Email, Website
Nice to have
• Modern, clean lines, classy
Should not have
• Business cards to be double-sided. Form keeps reverting to single-sided.

```html
<!DOCTYPE html>
<html lang="en">
<head>
<meta charset="utf-8">
<title>Brightwater Ledger &amp; Counsel – Business Cards</title>
<link href="https://fonts.googleapis.com/css2?family=Montserrat:wght@400;500;700&display=swap" rel="stylesheet">
<style>
  :root {
    --backdrop: #3b3634;
    --card-white: #ffffff;
    --card-black: #1c1c1c;
    --accent-grey: #8a8a8a;
    --ink: #111111;
    --ink-soft: #555555;
    --ink-light: #e8e8e8;
    --emboss: #2b2b2b;
  }
  * { box-sizing: border-box; margin: 0; padding: 0; }
  html, body { width: 1200px; height: 786px; overflow: hidden; }
  body {
    background: var(--backdrop);
    font-family: "Montserrat", sans-serif;
    position: relative;
  }
  .card {
    position: absolute;
    top: 245px;
    width: 520px;
    height: 297px;
    overflow: hidden;
    box-shadow: 0 10px 24px rgba(0,0,0,0.45);
  }
  .card--front { left: 60px; background: var(--card-white); }
  .card--back { left: 620px; background: var(--card-black); }

  .front-wave { position: absolute; inset: 0; width: 100%; height: 100%; }

  .brand {
    position: absolute;
    display: flex;
    align-items: center;
    gap: 10px;
    font-weight: 500;
    letter-spacing: 0.04em;
    text-transform: uppercase;
    line-height: 1.25;
  }
  .brand__square { width: 12px; height: 12px; flex: none; }
  .card--front .brand { top: 34px; right: 28px; color: var(--ink); font-size: 15px; }
  .card--front .brand__square { background: var(--ink); }
  .card--back .brand {
    top: 50%; left: 50%; transform: translate(-50%, -50%);
    color: var(--emboss); font-size: 22px; white-space: nowrap;
  }
  .card--back .brand__square { background: var(--emboss); width: 16px; height: 16px; }

  .edge-tab {
    position: absolute; left: 0; top: 110px;
    width: 9px; height: 30px; background: var(--card-black);
  }
  .person { position: absolute; left: 40px; top: 108px; }
  .person__name { font-weight: 700; font-size: 19px; color: var(--ink); }
  .person__title { font-size: 11px; color: var(--ink-soft); margin-top: 2px; }

  .contact {
    position: absolute; left: 32px; bottom: 24px;
    color: var(--ink-light); font-size: 12.5px; line-height: 1.45;
  }
  .contact__address { margin-bottom: 12px; }
  .contact__list { list-style: none; }
  .contact__item { display: flex; align-items: center; gap: 12px; }
  .contact__icon { width: 11px; height: 11px; flex: none; }
</style>
</head>
<body>

<section class="card card--front" aria-label="Business card front">
  <svg class="front-wave" viewBox="0 0 520 297" preserveAspectRatio="none" aria-hidden="true">
    <path fill="var(--accent-grey)" d="M250,168 C360,150 440,120 520,40 L520,110 C470,150 400,168 250,170 Z"/>
    <path fill="var(--card-black)" d="M0,297 L0,178 C70,150 140,176 220,172 C380,168 460,140 520,95 L520,297 Z"/>
  </svg>

  <div class="brand">
    <span class="brand__square"></span>
    <span class="brand__name">Brightwater Ledger<br>&amp; Counsel</span>
  </div>

  <span class="edge-tab"></span>
  <div class="person">
    <p class="person__name">Daniel Reyes</p>
    <p class="person__title">Owner</p>
  </div>

  <div class="contact">
    <p class="contact__address">Here is your full address<br>Road number #18 Lindenberg</p>
    <ul class="contact__list">
      <li class="contact__item">
        <svg class="contact__icon" viewBox="0 0 12 12" aria-hidden="true"><path fill="var(--ink-light)" d="M2.5 1 L4.5 1 L5.2 3.5 L4 4.4 C4.6 5.8 6.2 7.4 7.6 8 L8.5 6.8 L11 7.5 L11 9.5 C11 10.3 10.3 11 9.5 11 C5 11 1 7 1 2.5 C1 1.7 1.7 1 2.5 1 Z"/></svg>
        <span>+49 400 555 0182</span>
      </li>
      <li class="contact__item">
        <svg class="contact__icon" viewBox="0 0 12 12" aria-hidden="true"><rect x="0.5" y="2" width="11" height="8" fill="var(--ink-light)"/><path d="M0.5 2 L6 6.5 L11.5 2" fill="none" stroke="var(--card-black)" stroke-width="1"/></svg>
        <span>info@brightwaterledger.com</span>
      </li>
      <li class="contact__item">
        <svg class="contact__icon" viewBox="0 0 12 12" aria-hidden="true"><circle cx="6" cy="6" r="5" fill="none" stroke="var(--ink-light)" stroke-width="1.2"/><path d="M1 6 H11 M6 1 C3.5 3.5 3.5 8.5 6 11 M6 1 C8.5 3.5 8.5 8.5 6 11" fill="none" stroke="var(--ink-light)" stroke-width="0.9"/></svg>
        <span>www.brightwaterledger.com</span>
      </li>
    </ul>
  </div>
</section>

<section class="card card--back" aria-label="Business card back">
  <div class="brand">
    <span class="brand__square"></span>
    <span class="brand__name">Brightwater Ledger<br>&amp; Counsel</span>
  </div>
</section>

</body>
</html>
```